Meridale Family Law Firm Website Renovation

We need a website redesign in SquareSpace that is more modern, user friendly, on brand, less cluttered, easier to navigate, conveys clearly what our services are, and has clear, visible calls to action.

We would like to hire and work with the winning designer to complete the remaining pages of the site.

Target Market(s)

Couples looking for divorce representation or mediation who have a conscious, progressive mindset. They are self-aware and personal development plays an important role in their lives. They want an amicable interaction and aspire to have a healthy relationship after divorce.

Age range: 30-60
Income 100K+ household

Industry/Entity Type

Family Law

Font styles to use
Sans Serif

Colors
85acd3
33a6d7
50c0af
a0cd3a

Requirements
Must have
• Please see attached doc for full creative brief details.

"Changing the way people divorce" on top of site.
Images that show happy clients and that represent males and females. Diversity inclusion is also be important.
We are looking for warm, welcoming design and imagery.
Should not have
• Not heavily attorney focused.
Please see attached brief for full description.

```html
<!DOCTYPE html>
<html lang="en">
<head>
<meta charset="utf-8">
<title>Meridale Family Law &amp; Mediation</title>
<link rel="stylesheet" href="https://fonts.googleapis.com/css2?family=Mulish:ital,wght@0,300;0,400;0,600;0,700;1,400&display=swap">
<style>
:root{
  --green:#8cc63f;
  --lime:#a0cd3a;
  --teal:#50c0af;
  --blue:#33a6d7;
  --nav-blue:#2f8fd8;
  --ink:#2b2b2b;
  --body:#555;
  --grey-bg:#f4f4f4;
  --footer:#262626;
  --white:#fff;
  --head:'Mulish', Arial, sans-serif;
  --sans:'Mulish', Arial, sans-serif;
}
*{box-sizing:border-box;margin:0;padding:0}
html,body{width:1200px;height:4046px;overflow:hidden}
body{position:relative;background:var(--white);font-family:var(--sans);color:var(--ink)}
a{text-decoration:none}
.btn-grad{position:absolute;display:flex;align-items:center;justify-content:center;color:var(--white);font-family:var(--sans);font-weight:600;font-size:14px;letter-spacing:.5px;background:linear-gradient(90deg,var(--lime),var(--blue));border-radius:2px}

/* hero */
.hero{position:absolute;left:0;top:0;width:1200px;height:704px;background:linear-gradient(135deg,#92d030 0%,#86cc55 35%,#55bf98 70%,#2ab3e0 100%)}
.brand{position:absolute;left:115px;top:13px;width:172px;text-align:center;color:var(--white);font-family:var(--head)}
.brand .mark{width:92px;height:92px;border-radius:50%;background:rgba(255,255,255,.22);margin:0 auto 12px}
.brand .name{font-size:16px;font-weight:600;letter-spacing:4px;line-height:20px}
.brand .sub{font-size:9px;font-weight:600;letter-spacing:3px;margin-top:4px}
.nav{position:absolute;top:119px;left:366px;display:flex;font-size:15px;color:var(--white)}
.nav a{color:var(--white);height:32px;display:flex;align-items:center;padding:0 12px;margin-right:12px}
.nav a.active{background:var(--nav-blue);border-radius:2px;margin-right:14px}
.signup{position:absolute;left:958px;top:35px;width:129px;height:51px;border:2px solid var(--white);border-radius:26px;background:var(--lime);color:var(--white);font-size:15px;font-weight:600;display:flex;align-items:center;justify-content:center}
.tagline{position:absolute;left:112px;top:362px;font-size:15px;font-weight:600;letter-spacing:3px;text-transform:uppercase;color:var(--white)}
.hero h1{position:absolute;left:110px;top:400px;font-family:var(--head);font-weight:400;font-size:44px;line-height:66px;color:var(--white);letter-spacing:.5px}
.hero .appt{position:absolute;left:112px;top:558px;width:260px;height:56px;border:2px solid var(--white);color:var(--white);font-size:16px;font-weight:600;display:flex;align-items:center;justify-content:center;background:rgba(60,80,60,.25)}

/* intro */
.intro h2{position:absolute;left:112px;top:768px;font-family:var(--head);font-weight:400;font-size:36px}
.intro .copy{position:absolute;left:405px;top:770px;width:680px;font-size:14px;line-height:33px;color:var(--body)}
.intro .copy p+p{margin-top:33px}

/* services */
.services{position:absolute;left:0;top:1052px;width:1200px;height:1401px;background:var(--grey-bg)}
.photo{position:absolute}
.feature h3{position:absolute;font-family:var(--head);font-weight:400;font-size:33px;color:var(--ink)}
.feature .rule{position:absolute;width:63px;height:2px;background:var(--lime)}
.feature p{position:absolute;width:430px;font-size:12.5px;line-height:29px;color:var(--body);text-align:justify}

/* testimonial */
.quote-mark{position:absolute;left:116px;top:2510px;font-size:60px;color:#aaa;font-family:Georgia, serif}
.quote{position:absolute;left:157px;top:2522px;width:900px;font-style:italic;font-size:14px;line-height:37.5px;color:#444}
.quote-by{position:absolute;left:157px;top:2655px;font-size:16px;font-weight:600;color:var(--ink)}

/* contact */
.contact h2{position:absolute;left:112px;top:3245px;font-family:var(--head);font-weight:400;font-size:36px}
.contact .label{position:absolute;left:112px;font-size:17px;font-weight:600;color:var(--ink)}
.contact .val{position:absolute;left:112px;font-size:14px;color:#333}
.field{position:absolute;border:1px solid #bbb;border-radius:2px;background:var(--white);font-size:14px;color:#555;padding:14px 17px}
.submit{position:absolute;left:537px;top:3533px;width:126px;height:45px;background:var(--lime);color:var(--white);font-size:15px;font-weight:600;display:flex;align-items:center;justify-content:center}

/* footer */
.footer{position:absolute;left:0;top:3641px;width:1200px;height:405px;background:var(--footer);color:var(--white)}
.footer .brand{left:206px;top:45px;width:232px}
.footer .brand .mark{width:150px;height:150px;margin-bottom:18px}
.footer .brand .name{font-size:23px;letter-spacing:6px;line-height:28px}
.footer .brand .sub{font-size:12px;letter-spacing:4px;margin-top:6px}
.footer h4{position:absolute;top:36px;font-family:var(--head);font-weight:400;font-size:33px}
.footer ul{position:absolute;top:95px;list-style:none;font-size:13px;line-height:25.7px}
.copyright{position:absolute;left:0;width:1200px;top:350px;text-align:center;font-size:13px}
</style>
</head>
<body>

<header class="hero">
  <div class="brand">
    <div class="mark"></div>
    <div class="name">MERIDALE<br>FAMILY</div>
    <div class="sub">LAW &amp; MEDIATION</div>
  </div>
  <a class="signup">SIGNUP</a>
  <nav class="nav">
    <a class="active">Home</a><a>Services</a><a>About</a><a>Contact</a><a>FAQ</a><a>Blog</a><a>Resources</a><a>Testimonials</a>
  </nav>
  <div class="tagline">Changing the way people divorce</div>
  <h1>MERIDALE FAMILY LAW<br>&amp; MEDIATION</h1>
  <a class="appt">MAKE APPOINTMENT</a>
</header>

<section class="intro">
  <h2>What We Do</h2>
  <a class="btn-grad" style="left:112px;top:833px;width:124px;height:45px;font-size:15px">Read More</a>
  <div class="copy">
    <p>Divorce mediation - experienced family lawyers help families reach fair, workable agreements with-out the cost and damage of a conventional divorce process Divorce advice and representation - with the goal of minimizing financial and emotional costs to thefamilies.</p>
    <p>Our focus and intention is to help families and individuals navigate the divorce transition in a way that minimizes cost, pain, time, and collateral damage to children and to produce outcomes that are workable over the long term and result in healthy co-parenting families post-divorce.</p>
  </div>
</section>

<section class="services"></section>

<div class="feature">
  <div class="photo" role="img" aria-label="Couple meeting with a mediator at a table" style="left:112px;top:1110px;width:486px;height:385px;background:linear-gradient(135deg,#d9dde0,#8a8f95 55%,#3a3d42)"></div>
  <h3 style="left:638px;top:1142px">Divorce Mediation</h3>
  <div class="rule" style="left:638px;top:1200px"></div>
  <p style="left:639px;top:1226px">Mediation is possible when both spouses are willing to negotiate their divorce agreements in good faith, with the help of a neutral mediator. Meridale Family™ attorney-ediators are experienced family lawyers and are skilled at helping clients reach fair, workable agreements, with cost and damage of the conventional divorce process.</p>
  <a class="btn-grad" style="left:641px;top:1403px;width:148px;height:52px">READ MORE</a>
</div>

<div class="feature">
  <div class="photo" role="img" aria-label="Lawyer advising clients in an office" style="left:600px;top:1550px;width:487px;height:385px;background:linear-gradient(135deg,#b9c3c8,#6e6a62 50%,#2d2c2e)"></div>
  <h3 style="left:111px;top:1582px">Divorce Lawyer</h3>
  <div class="rule" style="left:112px;top:1640px"></div>
  <p style="left:112px;top:1666px">If mediation is not possible, you need a lawyer to advise, negotiate, and possibly advocate for you. Our experienced Meridale Family™ lawyers offer clear, confident, and highly effective advice and representation while attempting to minimize financial and emotional costs to you and Meridale your family.</p>
  <a class="btn-grad" style="left:112px;top:1843px;width:147px;height:51px">READ MORE</a>
</div>

<div class="feature">
  <div class="photo" role="img" aria-label="Smiling woman making a heart shape with her hands" style="left:112px;top:1990px;width:486px;height:385px;background:linear-gradient(135deg,#4a5a3a,#9a8a70 50%,#c9c2b0)"></div>
  <h3 style="left:638px;top:2022px">Our Story</h3>
  <div class="rule" style="left:638px;top:2080px"></div>
  <p style="left:639px;top:2106px">Many people don't want to add unnecessary financial and emotional costs to their divorce, but they need professional help to ensure they come away with a good parenting plan and fair financial outcomes.For these people, we offer Meridale Family™ divorce mediation or, when necessary, a Meridale Family™ lawyer.</p>
  <a class="btn-grad" style="left:641px;top:2282px;width:148px;height:52px">READ MORE</a>
</div>

<section class="testimonial">
  <div class="quote-mark">“</div>
  <p class="quote">I am so grateful for my experience with Meridale Family Law &amp; Mediation. I learned so much about myself and my capacity to love, grieve, and heal. You were so great at facilitating our difficult conversations, helping both of us feel validated, and coaching us on how to work well with each other moving forward in our new co-parenting relationship.</p>
  <div class="quote-by">Divorce mediation client</div>
</section>

<div class="photo" role="img" aria-label="Blurred photo of a girl with parents talking in the background" style="left:0;top:2736px;width:1200px;height:452px;background:linear-gradient(90deg,#7a7466,#4b4a44 40%,#35383a 70%,#2a2d30)"></div>

<section class="contact">
  <h2>Contact Us</h2>
  <div class="label" style="top:3320px">Address :</div>
  <div class="val" style="top:3354px"># 245 Lorem Ipsum Dummy Text Lorem ipsum</div>
  <div class="label" style="top:3407px">Email :</div>
  <div class="val" style="top:3442px">info@meridalefamilyfirm.com</div>
  <div class="label" style="top:3489px">Phone :</div>
  <div class="val" style="top:3523px">(555) 214-0387</div>

  <div class="field" style="left:539px;top:3266px;width:256px;height:48px">First Name :</div>
  <div class="field" style="left:810px;top:3266px;width:258px;height:48px">Last Name :</div>
  <div class="field" style="left:539px;top:3335px;width:529px;height:48px">Email :</div>
  <div class="field" style="left:539px;top:3399px;width:529px;height:116px">Message :</div>
  <a class="submit">SUBMIT</a>
</section>

<footer class="footer">
  <div class="brand">
    <div class="mark"></div>
    <div class="name">MERIDALE<br>FAMILY</div>
    <div class="sub">LAW &amp; MEDIATION</div>
  </div>
  <h4 style="left:609px">Links</h4>
  <ul style="left:611px">
    <li>Home</li><li>Services</li><li>About</li><li>Contact</li><li>FAQ</li><li>Blog</li><li>Resources</li><li>Testimonials</li>
  </ul>
  <h4 style="left:830px">Services</h4>
  <ul style="left:833px">
    <li>Meridale Family Law</li><li>Meridale Family Mediation</li>
  </ul>
  <div class="copyright">© Copyright 2020 Meridale Family Firm.All Rights Reserved</div>
</footer>

</body>
</html>
```